Business card for our large format printing and installation business

We want a professional looking business card for our business. We manufacture and install Signs.

On the back of the card add this info
Large Format Graphics Printing & Installations, Event Graphics, Banners, Posters, Vehicle Fleet Graphics, Boat Wraps, Wall Murals, Decals,Displays,Signs,Plaques,Digital Signs

On the Front of the card add the Tallowfern Signs logo, plus On the back of the card add the Orange Tallowfern Wraps logo. The 2 vector logos are attached to the design brief.

Target Market(s)

Local business owners

Contact Information for Business Card

Colors
f37122
f68d4e
f9ba93

Requirements
Must have
• On the Front of the card add the Tallowfern Signs logo, plus On the back of the card add the Orange Tallowfern Wraps logo. The 2 vector logos are attached to the design brief.

```html
<!DOCTYPE html>
<html lang="en">
<head>
<meta charset="utf-8">
<title>Tallowfern Signs – Business Card</title>
<link href="https://fonts.googleapis.com/css2?family=Work+Sans:wght@400;500;800&display=swap" rel="stylesheet">
<style>
  :root {
    --canvas: #e9e7e4;
    --card-dark: #2a2729;
    --logo-dark: #4d4a4c;
    --orange: #f37122;
    --orange-mid: #f68d4e;
    --orange-light: #f9ba93;
    --yellow: #f6e61f;
    --logo-gold: #f6a51f;
    --ink: #2b2b2b;
    --paper: #ffffff;
    --back-text: #d9d6d7;
  }
  * { margin: 0; padding: 0; box-sizing: border-box; }
  html, body { width: 1200px; height: 912px; overflow: hidden; }
  body {
    background: var(--canvas);
    font-family: "Work Sans", Arial, sans-serif;
    position: relative;
  }
  .card {
    position: absolute;
    left: 260px;
    width: 680px;
    height: 388px;
    border-radius: 22px;
    overflow: hidden;
    box-shadow: 0 10px 28px rgba(0,0,0,.22);
  }
  .card--back { top: 50px; background: var(--card-dark); }
  .card--front { top: 474px; background: var(--paper); }

  .back-content {
    position: absolute; inset: 0;
    display: flex; flex-direction: column; align-items: center; justify-content: center;
    text-align: center; padding: 0 56px;
  }
  .back-wordmark {
    font-weight: 800; font-size: 52px; letter-spacing: -1px; line-height: 1;
    color: var(--logo-dark);
  }
  .back-wraps {
    margin-top: 22px;
    font-weight: 800; font-size: 30px; letter-spacing: -0.5px; line-height: 1;
    color: var(--orange);
  }
  .back-rule {
    width: 120px; height: 2px; background: var(--orange-mid);
    margin: 22px 0 18px;
  }
  .back-services {
    font-size: 14px; line-height: 22px; color: var(--back-text);
  }
  .back-services strong { font-weight: 500; color: var(--orange-light); }

  .front-wave { position: absolute; inset: 0; width: 680px; height: 388px; }
  .front-wordmark {
    position: absolute; right: 34px; top: 28px;
    font-weight: 800; font-size: 34px; letter-spacing: -0.5px;
    color: var(--logo-gold);
  }
  .holder { position: absolute; left: 40px; top: 228px; }
  .holder__name {
    font-size: 27px; font-weight: 500; color: var(--orange);
    letter-spacing: 0.5px; text-transform: uppercase; line-height: 1.1;
  }
  .holder__role { font-size: 17px; color: var(--ink); margin-top: 4px; }
  .divider {
    position: absolute; left: 40px; right: 34px; top: 292px;
    height: 1.5px; background: var(--orange);
  }
  .contacts { position: absolute; left: 40px; top: 304px; list-style: none; }
  .contacts li {
    display: flex; align-items: center; gap: 10px;
    font-size: 17px; color: var(--ink); line-height: 25px;
  }
  .contacts svg { width: 13px; height: 13px; flex: none; }
  .address {
    position: absolute; right: 34px; top: 306px;
    text-align: right; font-size: 15px; color: var(--ink); line-height: 22px;
    font-style: normal;
  }
</style>
</head>
<body>

  <section class="card card--back" aria-label="Card back">
    <div class="back-content">
      <div class="back-wordmark">Tallowfern Signs</div>
      <div class="back-wraps">Tallowfern Wraps</div>
      <div class="back-rule"></div>
      <p class="back-services">
        <strong>Large Format Graphics Printing &amp; Installations</strong><br>
        Event Graphics · Banners · Posters · Vehicle Fleet Graphics · Boat Wraps<br>
        Wall Murals · Decals · Displays · Signs · Plaques · Digital Signs
      </p>
    </div>
  </section>

  <section class="card card--front" aria-label="Card front">
    <svg class="front-wave" viewBox="0 0 680 388" aria-hidden="true">
      <path d="M0 0 H680 V62 C590 138 430 122 300 122 C170 122 60 150 0 178 Z" fill="var(--card-dark)"/>
      <path d="M680 62 C590 138 430 122 300 122 C170 122 60 150 0 178 V206 C60 168 170 138 300 136 C440 134 600 140 680 70 Z" fill="var(--orange)"/>
      <path d="M0 206 C60 168 170 138 300 136 C200 142 90 170 40 220 C25 236 12 252 0 268 Z" fill="var(--yellow)"/>
      <path d="M0 206 C60 168 170 138 300 136 C190 144 80 176 0 222 Z" fill="var(--paper)"/>
    </svg>

    <div class="front-wordmark">Tallowfern Signs</div>

    <div class="holder">
      <p class="holder__name">Dorian Pell</p>
      <p class="holder__role">Director</p>
    </div>

    <div class="divider"></div>

    <ul class="contacts">
      <li>
        <svg viewBox="0 0 16 16"><path d="M4 1l3 3-2 2c1 2 3 4 5 5l2-2 3 3-2 3C7 14 2 9 1 3z" fill="var(--orange)"/></svg>
        06.41.73.19.82
      </li>
      <li>
        <svg viewBox="0 0 16 16"><rect x="1.5" y="3.5" width="13" height="9" fill="none" stroke="var(--orange)" stroke-width="1.6"/><path d="M1.5 3.5 8 9l6.5-5.5" fill="none" stroke="var(--orange)" stroke-width="1.6"/></svg>
        info@tallowfernsigns.com
      </li>
      <li>
        <svg viewBox="0 0 16 16"><circle cx="8" cy="8" r="6.5" fill="none" stroke="var(--orange)" stroke-width="1.4"/><ellipse cx="8" cy="8" rx="3" ry="6.5" fill="none" stroke="var(--orange)" stroke-width="1.2"/><path d="M1.5 8h13" stroke="var(--orange)" stroke-width="1.2"/></svg>
        www.tallowfernsigns.com
      </li>
    </ul>

    <address class="address">
      418 Alder Mill Road<br>
      Fernridge, PA 19388
    </address>
  </section>

</body>
</html>
```